Poster for a Bicycle show/Expo

We need a poster for a Bicycle show/Expo and sustainable transport. Exhibitors will sell bikes, cycling clothing, accessories, etc. ...
This show is annual and the Poster is for the 2015 edition.

The style must be modern, dynamic, bright colors.

Your concept must be compatible in a landscape format. (We will ourselves adaptations of different formats.)
Width: 210 mm
Height: 297 mm
It's necessary for us to have the source file (vector) for make, later, the different format (flyers, website, ...)

Content of the Poster:
- 1 big picture (no clip art)
- Big title: « Fête Roulix » (« Salon » or « Salon du » can be small and « Vélo » big.)
- Subtitle: « et de la mobilité douce »
- Date: « 8, 9 et 10 mai 2015 » or « 8-10 mai 2015 »
- Place: « Halle TRX - Quai Brenaz »
- Text line 1: « www.fete-roulix.ch - Entrée gratuite »
- Text line 2« Piste d’essais - Restauration sur place »
- Text line 3: « Ve 8 mai de 17h à 21h - Sa 9 mai de 10h à 20h - Di 10 mai de 10h à 18h »
- Please, leave a zone in the poster for sponsors logos
(The predominant information (most visible) are: « Fête Roulix » and « 8, 9 et 10 mai 2015 or 8-10 mai 2015 »)

Content of the big picture:
- from a cheap stock, like PixoBanq.com
- a bicycle in action or a detail of a bicycle (or a accessory) (no race bike)
- a modern picture with bright colors.
- if a person is on the picture, we prefer a men
- not an aerial view with cyclists in a landscape.

Some examples of poster of shows - with typo-title worked

http://www.bassinexpoville.com/Temp/IMG/F_a7c2e9b4d1f0836255e1b7a9c4d3f2e6812c9b0a4e5f7_200_296.png

http://qz4m.tolvanfoires.fr/Data/kmtolv_mer/block/F_9bd1c3e7f2a4605813c9e2d7b4a8f6c0d3e1a527f86c2.pdf
(page 2 of this PDF)

http://salons.marvelle-agenda.fr/images/marvelle-agenda/foires-salons/phototheque/expo-moto-brivanne/expo-moto-brivanne2012-affiche.jpg

http://www.drupaix.net/blog/wp-content/uploads/2007/03/affiche-foire-des-pages.jpg

http://www.voilemarine-club.com/wp-content/affiche-regate-2007.jpg

Hello,

For information, for your next versions, please, add the text "Piste d'essais".

- Text line 1: « www.fete-roulix.ch - Entrée gratuite »
- Text line 2: « Piste d’essais - Restauration sur place »
- Text line 3: « Ve 8 mai de 17h à 21h - Sa 9 mai de 10h à 20h - Di 10 mai de 10h à 18h »

Thanks,
Mathieu

Landscape

Sans Serif

```html
<!DOCTYPE html>
<html lang="fr">
<head>
<meta charset="utf-8">
<title>Fête Roulix et de la mobilité douce</title>
<link rel="stylesheet" href="https://fonts.googleapis.com/css2?family=Bebas+Neue&display=swap">
<style>
  :root {
    --paper: #ffffff;
    --ink: #141414;
    --title: #ffffff;
    --wall-light: #dccb98;
    --wall-mid: #b59d63;
    --wall-shadow: #6e5f3f;
    --sack-dark: #2a2e2c;
    --sack-teal: #3f7d82;
    --sack-white: #e4e0d6;
    --frame-grey: #b9bcbd;
    --sponsor: #e6e6e6;
  }
  html, body {
    margin: 0;
    padding: 0;
    overflow: hidden;
    background: var(--paper);
  }
  .poster {
    position: relative;
    width: 852px;
    height: 1200px;
    overflow: hidden;
    background: var(--paper);
    font-family: "Bebas Neue", "Oswald", sans-serif;
    color: var(--ink);
  }
  .hero-photo {
    position: absolute;
    left: 0;
    top: 149px;
    width: 852px;
    height: 704px;
    background:
      linear-gradient(180deg, rgba(0,0,0,0) 62%, rgba(25,22,18,0.55) 100%),
      radial-gradient(ellipse 34% 30% at 66% 66%, var(--sack-white) 0%, rgba(228,224,214,0) 100%),
      radial-gradient(ellipse 14% 30% at 96% 62%, var(--sack-white) 0%, rgba(228,224,214,0) 100%),
      radial-gradient(ellipse 30% 36% at 12% 70%, var(--sack-dark) 0%, rgba(42,46,44,0) 100%),
      radial-gradient(ellipse 22% 20% at 36% 55%, var(--sack-teal) 0%, rgba(63,125,130,0) 100%),
      radial-gradient(ellipse 40% 8% at 60% 36%, var(--frame-grey) 0%, rgba(185,188,189,0) 100%),
      linear-gradient(180deg, var(--wall-light) 0%, var(--wall-mid) 45%, var(--wall-shadow) 100%);
  }
  .headline {
    position: absolute;
    left: 40px;
    width: 772px;
    margin: 0;
    text-align: center;
    font-weight: 400;
    line-height: 1;
  }
  .headline--title {
    top: 726px;
    font-size: 160px;
    letter-spacing: 2px;
    color: var(--title);
  }
  .headline--subtitle {
    top: 858px;
    font-size: 88px;
    letter-spacing: 1px;
    color: var(--ink);
  }
  .info-line {
    position: absolute;
    left: 40px;
    width: 772px;
    margin: 0;
    text-align: center;
    font-size: 27px;
    line-height: 1;
    letter-spacing: 0.3px;
    color: var(--ink);
  }
  .info-line--hours { top: 947px; }
  .info-line--extras { top: 982px; }
  .event-date {
    position: absolute;
    left: 40px;
    width: 772px;
    top: 1024px;
    margin: 0;
    text-align: center;
    font-size: 64px;
    line-height: 1;
    letter-spacing: 1px;
  }
  .venue {
    position: absolute;
    left: 40px;
    width: 772px;
    top: 1086px;
    margin: 0;
    text-align: center;
    font-size: 28px;
    line-height: 1;
    letter-spacing: 0.5px;
  }
  .sponsors {
    position: absolute;
    left: 126px;
    top: 1134px;
    width: 600px;
    height: 44px;
    display: flex;
    justify-content: space-between;
    margin: 0;
    padding: 0;
    list-style: none;
  }
  .sponsors__slot {
    width: 104px;
    height: 44px;
    background: var(--sponsor);
  }
</style>
</head>
<body>
  <main class="poster">
    <div class="hero-photo" role="img" aria-label="Photo d'un vélo de ville gris appuyé contre un mur jaune écaillé, devant des sacs de farine"></div>
    <h1 class="headline headline--title">Fête Roulix</h1>
    <h2 class="headline headline--subtitle">Et de la mobilité douce</h2>
    <p class="info-line info-line--hours">VE 8 MAI DE 17H À 21H - SA 9 MAI DE 10H À 20H - DI 10 MAI DE 10H À 18H</p>
    <p class="info-line info-line--extras">PISTE D'ESSAIS - RESTAURATION SUR PLACE WWW.FETE-ROULIX.CH - ENTRÉE GRATUITE</p>
    <p class="event-date">8-10 MAI 2015</p>
    <p class="venue">HALLE TRX - QUAI BRENAZ</p>
    <ul class="sponsors" aria-label="Zone partenaires">
      <li class="sponsors__slot"></li>
      <li class="sponsors__slot"></li>
      <li class="sponsors__slot"></li>
      <li class="sponsors__slot"></li>
      <li class="sponsors__slot"></li>
    </ul>
  </main>
</body>
</html>
```